Business Card Design for Occupational Medicine Start Up Company

We need to design a professional business card. We are a healthcare company providing occupational medicine services to blue collar industries. We are professional, efficient and high quality service providers.

Target Market(s)

Blue Collar Industry: Shipbuilding, Ports, Trucking Companies; The Executives and Safety Officers for these companies

Industry/Entity Type

Healthcare

Contact Information for Business Card

Logo, Name, Title, Email, Phone

Other font styles liked:
• Please match our Brand Guide

Requirements
Must have
• Our Company Colors and Logo

```html
<!DOCTYPE html>
<html lang="en">
<head>
<meta charset="utf-8">
<title>Harborline Clinics – Business Card</title>
<link rel="stylesheet" href="https://fonts.googleapis.com/css2?family=Montserrat:wght@600;700&family=Roboto:wght@400;500&display=swap">
<style>
  :root {
    --navy: #1d2d8c;
    --navy-deep: #18257a;
    --sky: #3aa7e0;
    --gold: #f2b440;
    --white: #ffffff;
    --ink: #1b1b1b;
    --stage: #1c1c1c;
  }
  * { box-sizing: border-box; margin: 0; padding: 0; }
  html, body {
    width: 1200px; height: 900px; overflow: hidden;
    background: var(--stage);
  }
  .canvas { position: relative; width: 1200px; height: 900px; }
  .card {
    position: absolute; left: 290px; width: 620px; height: 354px;
    overflow: hidden;
    box-shadow: 0 10px 30px rgba(0,0,0,.5);
  }
  .card--front { top: 72px; background: var(--navy); }
  .card--back { top: 474px; background: var(--white); }

  .front-bands { position: absolute; top: 36px; left: 0; width: 100%; }
  .band { display: block; width: 100%; height: 8px; margin-bottom: 6px; }
  .band--gold { background: var(--gold); }
  .band--white { background: var(--white); }
  .band--sky { background: var(--sky); }

  .front-brand {
    position: absolute; top: 170px; left: 0; width: 100%;
    display: flex; align-items: center; justify-content: center; gap: 14px;
  }
  .brand-dot { width: 34px; height: 34px; border-radius: 50%; background: var(--white); }
  .brand-name {
    font-family: "Montserrat", sans-serif; font-weight: 700;
    font-size: 30px; letter-spacing: 1px; color: var(--white);
    text-transform: uppercase;
  }

  .back-brand {
    position: absolute; top: 48px; left: 52px;
    display: flex; align-items: center; gap: 22px;
  }
  .back-brand .brand-dot { width: 64px; height: 64px; background: var(--sky); }
  .back-brand .brand-name { color: var(--navy); font-size: 34px; }

  .contact {
    position: absolute; left: 272px; top: 196px;
    font-family: "Roboto", sans-serif; color: var(--ink);
  }
  .contact__name {
    font-family: "Montserrat", sans-serif; font-weight: 700;
    font-size: 24px; color: var(--navy);
  }
  .contact__title { font-size: 11px; margin-top: 2px; }
  .contact__list { list-style: none; margin-top: 34px; margin-left: 22px; }
  .contact__item {
    display: flex; align-items: center; gap: 16px;
    font-size: 14px; height: 24px;
  }
  .contact__icon { width: 14px; height: 14px; fill: var(--navy); }
</style>
</head>
<body>
<main class="canvas">

  <section class="card card--front" aria-label="Card front">
    <div class="front-bands" aria-hidden="true">
      <span class="band band--gold"></span>
      <span class="band band--white"></span>
      <span class="band band--sky"></span>
    </div>
    <div class="front-brand">
      <span class="brand-dot"></span>
      <span class="brand-name">Harborline Clinics</span>
    </div>
  </section>

  <section class="card card--back" aria-label="Card back">
    <div class="back-brand">
      <span class="brand-dot"></span>
      <span class="brand-name">Harborline Clinics</span>
    </div>
    <div class="contact">
      <p class="contact__name">Marisol</p>
      <p class="contact__title">Manager</p>
      <ul class="contact__list">
        <li class="contact__item">
          <svg class="contact__icon" viewBox="0 0 24 24" aria-hidden="true"><path d="M6.6 10.8a15 15 0 0 0 6.6 6.6l2.2-2.2a1 1 0 0 1 1-.25 11.4 11.4 0 0 0 3.6.57 1 1 0 0 1 1 1V20a1 1 0 0 1-1 1A17 17 0 0 1 3 4a1 1 0 0 1 1-1h3.5a1 1 0 0 1 1 1c0 1.25.2 2.45.57 3.57a1 1 0 0 1-.25 1z"/></svg>
          <span>555 201 4387</span>
        </li>
        <li class="contact__item">
          <svg class="contact__icon" viewBox="0 0 24 24" aria-hidden="true"><path d="M2 5h20v14H2z M3 6l9 7 9-7" fill="var(--navy)" stroke="var(--white)" stroke-width="1.5"/></svg>
          <span>info@harborlinecare.com</span>
        </li>
      </ul>
    </div>
  </section>

</main>
</body>
</html>
```